Copper & Wren Labels*

Hello :) I am needing labels for my herbal tea/petal product. I am a small producer for the local restaurants (edible flowers/micro herbs & dried product). I am hoping to sell the dried product online. It will be sold in batches as it is ready so quite small/boutique and the label needs to be somewhat generic for the range of produce I make.
Feels: no/minimal plastic, product is in a reusable mason jar, we use organic/regenerative principles from soil health to end product. Treading gently on the land. High quality i.e only fresh hand picked leaf tips for the tea.

```html
<!DOCTYPE html>
<html lang="en">
<head>
<meta charset="utf-8">
<title>Copper &amp; Wren – Jar Label</title>
<link rel="stylesheet" href="https://fonts.googleapis.com/css2?family=Playfair+Display:wght@600;700&family=Montserrat:wght@500;700&family=Great+Vibes&display=swap">
<style>
  :root {
    --bg: #e4e5e9;
    --label: #f4f4f2;
    --frame-fill: #f1f1ee;
    --frame-line: #5cbf4a;
    --cream-border: #ebe9dc;
    --brand-green: #3cb34a;
    --ink: #1b1b1b;
    --muted: #4a4a4a;
    --badge: #1e1e1e;
    --photo-blue: #5a55b8;
    --photo-pale: #e6e2ea;
    --photo-leaf: #a6c95e;
    --photo-warm: #e0844c;
  }
  * { box-sizing: border-box; margin: 0; padding: 0; }
  html, body { width: 1200px; height: 1200px; overflow: hidden; background: var(--bg); }
  .canvas { position: relative; width: 1200px; height: 1200px; }

  .label {
    position: absolute; left: 100px; top: 300px; width: 1000px; height: 600px;
    background: var(--label);
  }
  .label-frame { position: absolute; inset: 0; }

  .photo { position: absolute; }
  .photo.cornflower-blue {
    left: 150px; top: 190px; width: 210px; height: 240px; border-radius: 46% 40% 44% 50%;
    background: var(--photo-blue);
  }
  .photo.cornflower-white-top {
    left: 790px; top: 60px; width: 90px; height: 90px; border-radius: 50%;
    background: var(--photo-pale);
  }
  .photo.leaves {
    left: 740px; top: 195px; width: 80px; height: 60px; border-radius: 50% 50% 40% 40%;
    background: var(--photo-leaf);
  }
  .photo.flowers-right {
    left: 760px; top: 270px; width: 150px; height: 230px; border-radius: 48%;
    background: var(--photo-warm);
  }

  .brand {
    position: absolute; left: 360px; top: 140px; width: 320px;
    display: flex; flex-direction: column; align-items: center; gap: 14px;
  }
  .brand-dot { width: 80px; height: 80px; border-radius: 50%; background: var(--brand-green); }
  .brand-name {
    font-family: "Montserrat", sans-serif; font-weight: 700; font-size: 40px;
    color: var(--ink); letter-spacing: -0.5px;
  }

  .title {
    position: absolute; left: 330px; top: 285px; width: 380px; text-align: center;
    color: var(--ink); font-weight: normal;
  }
  .title-main { display: block; font-family: "Playfair Display", serif; font-weight: 700; font-size: 88px; line-height: 1; }
  .title-sub { display: block; margin-top: 4px; font-family: "Playfair Display", serif; font-weight: 600; font-size: 44px; line-height: 1.1; }
  .title-amp { font-family: "Great Vibes", cursive; font-size: 46px; margin-right: 10px; }

  .tagline {
    position: absolute; left: 470px; top: 475px; width: 280px;
    font-family: "Montserrat", sans-serif; font-weight: 500; font-size: 18px; line-height: 1.35;
    color: var(--muted);
  }
  .badge {
    position: absolute; left: 330px; top: 455px; width: 120px; height: 110px;
    border-radius: 50%; background: var(--badge);
  }
</style>
</head>
<body>
<main class="canvas">
  <section class="label">
    <svg class="label-frame" viewBox="0 0 1000 600" width="1000" height="600" aria-hidden="true">
      <path d="M110 40 H330 Q360 40 380 20 Q500 -10 620 20 Q640 40 670 40 H890 V560 H670 Q640 560 620 580 Q500 610 380 580 Q360 560 330 560 H110 Z"
            fill="var(--frame-fill)" stroke="var(--cream-border)" stroke-width="22"/>
      <path d="M120 50 H330 Q365 50 388 30 Q500 2 612 30 Q635 50 670 50 H880 V550 H670 Q635 550 612 570 Q500 598 388 570 Q365 550 330 550 H120 Z"
            fill="none" stroke="var(--frame-line)" stroke-width="3"/>
    </svg>

    <div class="photo cornflower-blue" role="img" aria-label="Photo of blue cornflowers with green leaves"></div>
    <div class="photo cornflower-white-top" role="img" aria-label="Photo of a white and purple cornflower"></div>
    <div class="photo leaves" role="img" aria-label="Photo of fresh tea leaf tips"></div>
    <div class="photo flowers-right" role="img" aria-label="Photo of a white cornflower and an orange calendula"></div>

    <div class="brand">
      <span class="brand-dot"></span>
      <span class="brand-name">fernhollow</span>
    </div>

    <h1 class="title">
      <span class="title-main">Copper</span>
      <span class="title-sub"><span class="title-amp">&amp;</span>Wren</span>
    </h1>

    <div class="badge"></div>
    <p class="tagline">Grown, harvested and dried chemical free on our farm in the Wren Valley</p>
  </section>
</main>
</body>
</html>
```